Fernwick Ridge Glide Treks

We offer guided cross country ( Nordic ) skiing tours in the National Forest bordering Silverpine National Park. I need a website that attracts individuals by using photos ( provided by me ) , brief descriptions of what to expect, a place with phone numbers to call for a tour, and I would like the website to feature the same color scheme as the logo, which I will upload.

```html
<!DOCTYPE html>
<html lang="en">
<head>
<meta charset="utf-8">
<title>Fernwick Ridge Glide Treks</title>
<link rel="stylesheet" href="https://fonts.googleapis.com/css2?family=Poppins:wght@600;700&family=Work+Sans:wght@400;500;600;700&display=swap">
<style>
:root{
  --purple:#7781bf;
  --purple-dark:#5f69a8;
  --lavender:#d0d6eb;
  --lavender-soft:#e7eaf4;
  --page:#f7f8fc;
  --ink:#0d0d12;
  --text:#5d5f6b;
  --white:#ffffff;
}
*{box-sizing:border-box;margin:0;padding:0}
html,body{width:1200px;height:3263px;overflow:hidden}
body{position:relative;background:var(--page);font-family:"Work Sans",sans-serif;color:var(--text)}
.abs{position:absolute}
.btn{position:absolute;display:flex;align-items:center;justify-content:center;background:var(--purple);color:var(--white);border-radius:30px;font:700 15px "Work Sans",sans-serif;letter-spacing:.3px;text-transform:uppercase}
.heading{position:absolute;left:0;width:1200px;text-align:center;font:700 40px "Poppins",sans-serif;color:var(--ink);letter-spacing:.2px}

/* header */
.topline{left:0;top:0;width:1200px;height:4px;background:var(--purple);z-index:4}
.header{left:0;top:4px;width:1200px;height:82px;background:var(--white);z-index:3}
.brand{left:85px;top:-11px;width:174px;height:174px;border-radius:50%;background:var(--white);display:flex;align-items:center;justify-content:center;z-index:5}
.brand-mark{width:136px;height:136px;border-radius:50%;border:3px solid var(--ink);display:flex;align-items:center;justify-content:center;text-align:center;font:700 15px "Work Sans",sans-serif;color:var(--ink);line-height:1.25;padding:10px;text-transform:uppercase}
.nav{left:347px;top:30px;display:flex;gap:27px;font:600 15px "Work Sans",sans-serif;color:var(--ink);text-transform:uppercase}
.nav .active{color:var(--purple)}
.contact-btn{left:951px;top:16px;width:136px;height:49px}

/* hero */
.hero{left:0;top:86px;width:1200px;height:634px;background:linear-gradient(180deg,#2a63c4 0%,#4f88d6 30%,#a9c6ea 48%,#e9eef5 60%,#c9d1dc 80%,#6f7682 100%)}
.hero-edge{left:0;top:560px;width:1200px;height:170px}
.hero-title{left:0;top:286px;width:1200px;text-align:center;font:700 42px "Poppins",sans-serif;color:var(--white)}
.hero-sub{left:300px;top:346px;width:600px;text-align:center;font:700 19px/28px "Work Sans",sans-serif;color:var(--white)}
.hero-btn{left:523px;top:422px;width:152px;height:49px}

/* about */
.about-bg{left:0;top:720px;width:1200px;height:686px;background:linear-gradient(180deg,#f7f8fc 0%,#eef0f6 40%,#e3e6ef 100%)}
.about-photo{left:126px;top:804px;width:406px;height:406px;border-radius:50%;background:radial-gradient(circle at 50% 70%,#f1f3f7 0%,#d9dde4 45%,#5e6864 80%,#3f4946 100%);border:6px solid var(--white)}
.about-arc{left:110px;top:798px;width:420px;height:420px}
.about-title{left:600px;top:824px;font:700 38px "Poppins",sans-serif;color:var(--ink)}
.about-text{left:600px;top:900px;width:487px;font:400 15px/25px "Work Sans",sans-serif;text-align:justify}
.about-text p+p{margin-top:15px}
.about-btn{left:600px;top:1126px;width:154px;height:50px}

/* expect */
.expect-band{left:0;top:1305px;width:1200px;height:640px}
.card{position:absolute;top:1523px;width:312px;height:291px;background:var(--white);border-radius:4px;text-align:center}
.card svg{margin-top:30px}
.card h3{margin-top:12px;font:600 19px "Work Sans",sans-serif;color:var(--ink);text-transform:uppercase;letter-spacing:.3px}
.card p{margin:18px 10px 0;font:400 14px/26px "Work Sans",sans-serif}

/* offer */
.tour{position:absolute;top:2121px;width:471px;height:333px}
.tour-frame{position:absolute;left:17px;top:0;width:454px;height:316px;border:5px solid var(--purple);border-radius:6px}
.tour-photo{position:absolute;left:0;top:17px;width:454px;height:316px;border-radius:4px}
.tour-label{position:absolute;left:30px;bottom:20px;display:flex;align-items:center;gap:14px;font:700 16px "Work Sans",sans-serif;color:var(--white);text-transform:uppercase;letter-spacing:.3px}

/* contact */
.contact-band{left:0;top:2549px;width:1200px;height:375px;background:linear-gradient(180deg,#c7cfe8 0%,#d6dcee 55%,#e8ebf4 100%)}
.contact-text{left:140px;top:2686px;width:920px;text-align:center;font:400 15px/26px "Work Sans",sans-serif}
.contact-btn2{left:508px;top:2800px;width:184px;height:49px}

/* footer */
.footer{left:0;top:2924px;width:1200px;height:339px;background:#f6f7fb}
.foot-brand{left:112px;top:2987px;width:188px;height:188px;border-radius:50%;border:3px solid var(--ink);display:flex;align-items:center;justify-content:center;text-align:center;font:700 19px/1.3 "Work Sans",sans-serif;color:var(--ink);text-transform:uppercase;padding:20px}
.col{position:absolute;top:2978px}
.col h4{font:700 17px "Work Sans",sans-serif;color:var(--ink);text-transform:uppercase;margin-bottom:17px}
.col li{list-style:none;display:flex;align-items:flex-start;gap:18px;font:400 15px/29px "Work Sans",sans-serif}
.col li svg{flex:none;margin-top:8px}
.rule{left:111px;top:3199px;width:976px;height:1px;background:#d9dbe3}
.copy{left:405px;top:3222px;font:400 13px "Work Sans",sans-serif}
.copy b{color:var(--ink);font-weight:700}
.social{position:absolute;top:3212px;width:38px;height:38px;border-radius:50%;background:var(--purple)}
</style>
</head>
<body>

<div class="abs topline"></div>
<header class="abs header">
  <nav class="abs nav">
    <span class="active">Home</span><span>About Me</span><span>What Expect To</span><span>Tour Plans</span><span>Events</span>
  </nav>
  <div class="btn contact-btn">Contact</div>
</header>
<div class="abs brand"><div class="brand-mark">Fernwick Ridge Glide Treks</div></div>

<section>
  <div class="abs hero" role="img" aria-label="Snow-covered mountain peak under a blue sky with clouds"></div>
  <svg class="abs hero-edge" viewBox="0 0 1200 170" preserveAspectRatio="none" aria-hidden="true">
    <path d="M0 58 Q600 52 1200 58 L1200 64 Q600 58 0 64 Z" fill="#f7f8fc"/>
    <path d="M0 50 Q600 240 1200 50 L1200 170 L0 170 Z" fill="#f7f8fc"/>
  </svg>
  <h1 class="abs hero-title">FERNWICK RIDGE GLIDE TREKS</h1>
  <p class="abs hero-sub">Lorem ipsum dolor sit amet, consectetur adipiscing elit sed do eiusmod tempor incididunta.</p>
  <div class="btn hero-btn">Get Started</div>
</section>

<section>
  <div class="abs about-bg" role="img" aria-label="Faint backdrop of snow-laden evergreen trees"></div>
  <svg class="abs about-arc" viewBox="0 0 420 420" aria-hidden="true">
    <path d="M210 8 A202 202 0 0 0 210 412" fill="none" stroke="var(--purple)" stroke-width="9"/>
  </svg>
  <div class="abs about-photo" role="img" aria-label="Skier on a snowy trail between snow-covered pine trees"></div>
  <h2 class="abs about-title">ABOUT ME</h2>
  <div class="abs about-text">
    <p>Lorem ipsum dolor sit amet, consectetur adipiscing elit, sed do eiusmod tempor incididunt ut labore et dolore magna aliqua. Ut enim ad minim veniam, quis nostrud exercitation ullamco laboris nisi ut aliquip ex ea commodo consequat.</p>
    <p>Duis aute irure dolor in reprehenderit in voluptate velit esse cillum dolore eu fugiat nulla pariatur. Excepteur sint occaecat cupidatat non proident, sunt in culpa qui officia.</p>
  </div>
  <div class="btn about-btn">Learn More</div>
</section>

<section>
  <svg class="abs expect-band" viewBox="0 0 1200 640" preserveAspectRatio="none" aria-hidden="true">
    <path d="M0 105 Q600 -110 1200 105 L1200 540 Q600 760 0 540 Z" fill="var(--lavender)"/>
  </svg>
  <h2 class="heading" style="top:1424px">WHAT EXPECT TO</h2>

  <div class="card" style="left:111px">
    <svg width="60" height="64" viewBox="0 0 60 64" aria-hidden="true">
      <g stroke="var(--purple)" stroke-width="5" stroke-linecap="round" fill="none">
        <path d="M30 4V60M6 18L54 46M54 18L6 46"/>
        <path d="M22 8L30 16L38 8M22 56L30 48L38 56M4 28L15 25L12 14M56 36L45 39L48 50M56 28L45 25L48 14M4 36L15 39L12 50"/>
      </g>
    </svg>
    <h3>Lorem Ipsum Dol</h3>
    <p>Sed ut perspiciatis unde omnis iste nat us error sit voluptatem accusantium do loremque laudantium, totam rem ape riam, eaque ipsa quae.</p>
  </div>
  <div class="card" style="left:443px">
    <svg width="64" height="64" viewBox="0 0 64 64" aria-hidden="true">
      <g stroke="var(--purple)" stroke-width="2" fill="none" stroke-linecap="round">
        <rect x="6" y="14" width="30" height="46" rx="2"/>
        <path d="M12 24h4M12 34h4M12 44h4M12 54h4M20 24h11M20 34h11M20 44h11M20 54h11"/>
        <circle cx="47" cy="18" r="13"/><path d="M47 10v8l5 4"/>
      </g>
    </svg>
    <h3>Lorem Ipsum Dol</h3>
    <p>Sed ut perspiciatis unde omnis iste nat us error sit voluptatem accusantium do loremque laudantium, totam rem ape riam, eaque ipsa quae.</p>
  </div>
  <div class="card" style="left:775px">
    <svg width="64" height="64" viewBox="0 0 64 64" aria-hidden="true">
      <g stroke="var(--purple)" stroke-width="2.5" fill="none" stroke-linecap="round">
        <circle cx="46" cy="8" r="5"/>
        <path d="M20 20l14 -4 8 6 -8 12 8 10M34 34l-12 2M8 14l14 10M6 52l50 10"/>
      </g>
    </svg>
    <h3>Lorem Ipsum Dol</h3>
    <p>Sed ut perspiciatis unde omnis iste nat us error sit voluptatem accusantium do loremque laudantium, totam rem ape riam, eaque ipsa quae.</p>
  </div>
</section>

<section>
  <h2 class="heading" style="top:2027px">WE OFFER GUIDED</h2>
  <div class="tour" style="left:111px">
    <div class="tour-frame"></div>
    <div class="tour-photo" role="img" aria-label="Snowy forest of evergreens with mountain ranges behind" style="background:linear-gradient(180deg,#c9ccd2 0%,#8d939c 35%,#e1e4ea 55%,#5a6068 80%,#2e3338 100%)">
      <div class="tour-label">National Forest Bordering
        <svg width="18" height="10" viewBox="0 0 18 10" aria-hidden="true"><path d="M0 5h15M11 1l4 4-4 4" stroke="#fff" stroke-width="2.4" fill="none"/></svg>
      </div>
    </div>
  </div>
  <div class="tour" style="left:616px">
    <div class="tour-frame"></div>
    <div class="tour-photo" role="img" aria-label="Snowy clearing between tall pine trees in a national park" style="background:linear-gradient(180deg,#b9c0c8 0%,#54605a 30%,#2f3a33 55%,#b9bfca 80%,#9ea5b2 100%)">
      <div class="tour-label">Silverpine National Park
        <svg width="18" height="10" viewBox="0 0 18 10" aria-hidden="true"><path d="M0 5h15M11 1l4 4-4 4" stroke="#fff" stroke-width="2.4" fill="none"/></svg>
      </div>
    </div>
  </div>
</section>

<section>
  <div class="abs contact-band" role="img" aria-label="Faded snowy mountain peak in lavender tones"></div>
  <h2 class="heading" style="top:2612px">CONTACT NOW</h2>
  <p class="abs contact-text">Sed ut perspiciatis unde omnis iste natus error sit voluptatem accusantium doloremque laudantium, totam rem aperiam, eaque ipsa quae ab illo inventore veritatis et quasi architecto beatae vitae dicta sunt explicabo. Nemo enim ipsam voluptatem quia voluptas sit aspernatur aut odit aut fugit sed quia consequuntura.</p>
  <div class="btn contact-btn2">Call For A Tour</div>
</section>

<footer>
  <div class="abs footer"></div>
  <div class="abs foot-brand">Fernwick Ridge Glide Treks</div>

  <div class="col" style="left:394px">
    <h4>Quick Links</h4>
    <ul>
      <li><svg width="13" height="13" viewBox="0 0 14 14"><circle cx="7" cy="7" r="7" fill="var(--purple)"/><path d="M4 7h6M7 4l3 3-3 3" stroke="#fff" stroke-width="1.6" fill="none"/></svg>Home</li>
      <li><svg width="13" height="13" viewBox="0 0 14 14"><circle cx="7" cy="7" r="7" fill="var(--purple)"/><path d="M4 7h6M7 4l3 3-3 3" stroke="#fff" stroke-width="1.6" fill="none"/></svg>About Me</li>
      <li><svg width="13" height="13" viewBox="0 0 14 14"><circle cx="7" cy="7" r="7" fill="var(--purple)"/><path d="M4 7h6M7 4l3 3-3 3" stroke="#fff" stroke-width="1.6" fill="none"/></svg>What Expect To</li>
      <li><svg width="13" height="13" viewBox="0 0 14 14"><circle cx="7" cy="7" r="7" fill="var(--purple)"/><path d="M4 7h6M7 4l3 3-3 3" stroke="#fff" stroke-width="1.6" fill="none"/></svg>Tour Plans</li>
      <li><svg width="13" height="13" viewBox="0 0 14 14"><circle cx="7" cy="7" r="7" fill="var(--purple)"/><path d="M4 7h6M7 4l3 3-3 3" stroke="#fff" stroke-width="1.6" fill="none"/></svg>Events</li>
    </ul>
  </div>
  <div class="col" style="left:635px">
    <h4>About Links</h4>
    <ul>
      <li><svg width="13" height="13" viewBox="0 0 14 14"><circle cx="7" cy="7" r="7" fill="var(--purple)"/><path d="M4 7h6M7 4l3 3-3 3" stroke="#fff" stroke-width="1.6" fill="none"/></svg>Site Map</li>
      <li><svg width="13" height="13" viewBox="0 0 14 14"><circle cx="7" cy="7" r="7" fill="var(--purple)"/><path d="M4 7h6M7 4l3 3-3 3" stroke="#fff" stroke-width="1.6" fill="none"/></svg>Privacy Policy</li>
      <li><svg width="13" height="13" viewBox="0 0 14 14"><circle cx="7" cy="7" r="7" fill="var(--purple)"/><path d="M4 7h6M7 4l3 3-3 3" stroke="#fff" stroke-width="1.6" fill="none"/></svg>Terms Of Use</li>
      <li><svg width="13" height="13" viewBox="0 0 14 14"><circle cx="7" cy="7" r="7" fill="var(--purple)"/><path d="M4 7h6M7 4l3 3-3 3" stroke="#fff" stroke-width="1.6" fill="none"/></svg>Legal Support</li>
    </ul>
  </div>
  <div class="col" style="left:865px">
    <h4>Contact</h4>
    <ul>
      <li><svg width="13" height="14" viewBox="0 0 12 16"><path d="M6 0a6 6 0 0 1 6 6c0 4-6 10-6 10S0 10 0 6a6 6 0 0 1 6-6z" fill="var(--purple)"/><circle cx="6" cy="6" r="2.2" fill="#fff"/></svg><span>465, Lorum Ipsum Dol,<br>Nordic</span></li>
      <li><svg width="13" height="13" viewBox="0 0 16 16"><path d="M3 1l3 3-2 2c1 2 3 4 5 5l2-2 3 3-2 3C6 15 1 10 1 3z" fill="var(--purple)"/></svg>123 - 456 - 7890</li>
      <li><svg width="14" height="11" viewBox="0 0 16 12"><rect width="16" height="12" rx="1" fill="var(--purple)"/><path d="M1 1l7 6 7-6" stroke="#fff" stroke-width="1.3" fill="none"/></svg>info@fernwickridge.com</li>
    </ul>
  </div>

  <div class="abs rule"></div>
  <p class="abs copy">© 2021 <b>FERNWICK RIDGE GLIDE TREKS</b>. All Rights Reserved</p>
  <div class="social" style="left:970px"></div>
  <div class="social" style="left:1010px"></div>
  <div class="social" style="left:1050px"></div>
</footer>

</body>
</html>
```